Business Card Design Project

Hi,

We are a new modern sheet metal business and I require a business card for our sales reps.

The card should be double sided and standout in a crowd.

I have attached our logo and our website is www.plyform.com.au.

Please ask if you have any further questions
Updates

hi everyone, 

I'm wondering if we can try to lighten the cards mood.  Everyone is using black and I'm not sure how that would be accepted in real life.

Gordon

Reason: Still No receiving what I was hoping for.

Industry/Entity Type

Business

Requirements
Must have
• double sided

```html
<!DOCTYPE html>
<html lang="en">
<head>
<meta charset="utf-8">
<title>Quenwick Sheetmetal – Business Card</title>
<link rel="stylesheet" href="https://fonts.googleapis.com/css2?family=Roboto+Condensed:wght@400;700&display=swap">
<style>
  :root {
    --backdrop: #e4e4e4;
    --steel-light: #f1f2f3;
    --steel-mid: #c9cbce;
    --steel-dark: #a7aaae;
    --brand-blue: #253a8c;
    --ink-grey: #5b5e63;
    --ink-white: #ffffff;
    --text-shadow: rgba(40, 42, 46, 0.55);
  }
  * { margin: 0; padding: 0; box-sizing: border-box; }
  html, body {
    width: 1200px;
    height: 902px;
    overflow: hidden;
    background: var(--backdrop);
    font-family: "Roboto Condensed", "Arial Narrow", sans-serif;
  }
  .sheet {
    width: 1200px;
    height: 902px;
    display: flex;
    flex-direction: column;
    align-items: center;
    justify-content: center;
    gap: 56px;
  }
  .card {
    position: relative;
    width: 600px;
    height: 367px;
    border-radius: 4px;
    overflow: hidden;
    background: linear-gradient(135deg, var(--steel-light) 0%, var(--steel-mid) 45%, var(--steel-light) 70%, var(--steel-dark) 100%);
    box-shadow: 0 6px 18px rgba(0, 0, 0, 0.18);
  }
  .brand-name {
    display: flex;
    align-items: center;
    color: var(--brand-blue);
    font-weight: 700;
    line-height: 1;
    white-space: nowrap;
  }
  .brand-mark {
    flex: none;
    background: var(--brand-blue);
  }
  .services {
    color: var(--ink-grey);
    font-weight: 700;
    white-space: nowrap;
  }

  /* Front side */
  .card-front .brand-name {
    position: absolute;
    left: 40px;
    top: 74px;
    gap: 16px;
    font-size: 50px;
  }
  .card-front .brand-mark { width: 28px; height: 28px; }
  .card-front .services {
    position: absolute;
    left: 40px;
    top: 150px;
    font-size: 22px;
    letter-spacing: 0.5px;
  }

  /* Back side */
  .card-back .mini-brand {
    position: absolute;
    left: 34px;
    top: 52px;
  }
  .card-back .brand-name {
    gap: 8px;
    font-size: 24px;
  }
  .card-back .brand-mark { width: 14px; height: 14px; }
  .card-back .services {
    margin-top: 8px;
    font-size: 11px;
  }
  .contact-lines {
    position: absolute;
    right: 40px;
    top: 48px;
    color: var(--ink-white);
    font-size: 28px;
    line-height: 1.25;
    text-shadow: 1px 1px 2px var(--text-shadow);
  }
  .address-lines {
    position: absolute;
    left: 0;
    right: 0;
    top: 206px;
    text-align: center;
    color: var(--ink-white);
    font-size: 27px;
    line-height: 1.3;
    text-shadow: 1px 1px 2px var(--text-shadow);
  }
</style>
</head>
<body>
<main class="sheet">
  <section class="card card-front" aria-label="Card front">
    <div class="brand-name"><span class="brand-mark"></span>QUENWICK SHEETMETAL</div>
    <p class="services">Flashings | Gutter | Rainwater Goods</p>
  </section>

  <section class="card card-back" aria-label="Card back">
    <div class="mini-brand">
      <div class="brand-name"><span class="brand-mark"></span>QUENWICK SHEETMETAL</div>
      <p class="services">Flashings | Gutter | Rainwater Goods</p>
    </div>
    <div class="contact-lines">
      <p>Tel : 3555 0142</p>
      <p>Fax : 3555 0187</p>
    </div>
    <div class="address-lines">
      <p>42 Quarry Road , Redbank Q 4301</p>
      <p>Po Box : 87 Redbank Q 4301</p>
      <p>www.quenwick.com.au</p>
    </div>
  </section>
</main>
</body>
</html>
```